Real Estate Sales Brokerage

Design a modern and fresh looking standard size business card, incorporate our logo's color scheme and modern appearance with head shot photo on front side and incorporate our log on the back side

Target Market(s)

Residential Home sales

Industry/Entity Type

Real Estate Agent

Font styles to use
Sans Serif

Colors

Designer to choose colors to be used in the design.

Requirements
Must have
• fresh, modern, not too busy, incorporate head shot in front of the card, incorporate logo in front and back of the card. Use logo design scheme as appropriate.
Nice to have
• horizontal and vertical options to compare would be nice.

```html
<!DOCTYPE html>
<html lang="en">
<head>
<meta charset="utf-8">
<title>Meridian Hearth Realty – Business Card</title>
<link href="https://fonts.googleapis.com/css2?family=Questrial&display=swap" rel="stylesheet">
<style>
  :root {
    --stage: #d9d9d9;
    --card-white: #ffffff;
    --olive: #5f5e37;
    --olive-deep: #2b2b1c;
    --olive-text: #56552f;
    --gold: #f2d64b;
    --gold-line: #c9ac2c;
    --ink: #2a2a1c;
    --photo-a: #3f5a3a;
    --photo-b: #8a9aa8;
    --photo-c: #2f4f8f;
  }
  * { box-sizing: border-box; margin: 0; padding: 0; }
  html, body { width: 1200px; height: 1200px; overflow: hidden; }
  body {
    background: linear-gradient(160deg, #cfcfcf 0%, #e6e6e6 100%);
    font-family: "Questrial", "Century Gothic", sans-serif;
    position: relative;
  }
  .card {
    position: absolute;
    left: 150px;
    width: 900px;
    height: 514px;
    overflow: hidden;
    box-shadow: 0 10px 28px rgba(0,0,0,0.22);
  }
  /* back side */
  .card-back { top: 60px; background: var(--card-white); }
  .brand {
    position: absolute;
    left: 50%; top: 50%;
    transform: translate(-50%, -50%);
    display: flex; align-items: center; gap: 26px;
  }
  .brand-mark {
    width: 64px; height: 64px;
    background: var(--olive);
  }
  .brand-name {
    color: var(--olive-text);
    font-size: 46px;
    line-height: 1.08;
    letter-spacing: 2px;
    text-transform: uppercase;
  }
  /* front side */
  .card-front { top: 626px; background: var(--olive); }
  .headshot {
    position: absolute;
    right: 0; top: 0;
    width: 560px; height: 514px;
    background:
      radial-gradient(ellipse at 55% 80%, var(--photo-c) 0%, rgba(47,79,143,0) 55%),
      linear-gradient(180deg, var(--photo-a) 0%, var(--photo-b) 60%, #b8a894 100%);
  }
  .panel-depth {
    position: absolute; left: 0; top: 0;
    width: 900px; height: 514px;
  }
  .contact-panel {
    position: absolute;
    left: 150px; top: 118px;
    width: 430px; height: 300px;
    background: var(--gold);
    display: flex; flex-direction: column;
  }
  .contact-row {
    flex: 1;
    display: flex; align-items: center;
    border-bottom: 1.5px solid var(--gold-line);
  }
  .contact-row:last-child { border-bottom: none; }
  .contact-icon {
    width: 70px; height: 100%;
    display: flex; align-items: center; justify-content: center;
    border-right: 1.5px solid var(--gold-line);
  }
  .contact-icon svg { width: 24px; height: 24px; fill: var(--ink); }
  .contact-text {
    padding-left: 26px;
    color: var(--ink);
    font-size: 25px;
    letter-spacing: 0.5px;
  }
  .contact-name .contact-text { font-size: 30px; }
</style>
</head>
<body>

<section class="card card-back" aria-label="Card back">
  <div class="brand">
    <div class="brand-mark"></div>
    <div class="brand-name">Meridian<br>Hearth<br>Realty</div>
  </div>
</section>

<section class="card card-front" aria-label="Card front">
  <div class="headshot" role="img" aria-label="Head shot of the agent in a blue suit, outdoors"></div>

  <svg class="panel-depth" viewBox="0 0 900 514" aria-hidden="true">
    <polygon points="0,230 150,118 150,418 580,418 470,514 0,514" fill="var(--olive-deep)"/>
  </svg>

  <div class="contact-panel">
    <div class="contact-row contact-name">
      <div class="contact-icon">
        <svg viewBox="0 0 24 24"><circle cx="12" cy="7" r="5"/><path d="M2 23c0-6 4-9 10-9s10 3 10 9z"/></svg>
      </div>
      <div class="contact-text">Your Name</div>
    </div>
    <div class="contact-row">
      <div class="contact-icon">
        <svg viewBox="0 0 24 24"><path d="M6.6 10.8a15.1 15.1 0 0 0 6.6 6.6l2.2-2.2c.3-.3.7-.4 1-.2 1.1.4 2.3.6 3.6.6.6 0 1 .4 1 1V20c0 .6-.4 1-1 1A17 17 0 0 1 3 4c0-.6.4-1 1-1h3.5c.6 0 1 .4 1 1 0 1.3.2 2.5.6 3.6.1.3 0 .7-.2 1z"/></svg>
      </div>
      <div class="contact-text">0123456789</div>
    </div>
    <div class="contact-row">
      <div class="contact-icon">
        <svg viewBox="0 0 24 24"><path d="M2 5h20v14H2z M3.5 6.5 12 13l8.5-6.5" fill="var(--ink)"/><path d="M3.5 6.5 12 13l8.5-6.5" fill="none" stroke="var(--gold)" stroke-width="1.6"/></svg>
      </div>
      <div class="contact-text">info@meridianhearth.com</div>
    </div>
    <div class="contact-row">
      <div class="contact-icon">
        <svg viewBox="0 0 24 24"><circle cx="12" cy="12" r="10"/><path d="M2 12h20M12 2v20M5 6.5h14M5 17.5h14M12 2c-4 4-4 16 0 20M12 2c4 4 4 16 0 20" fill="none" stroke="var(--gold)" stroke-width="1.3"/></svg>
      </div>
      <div class="contact-text">www.mhrealty.com</div>
    </div>
  </div>
</section>

</body>
</html>
```